Business Card Design for Transmission Repair / Automotive Shop

Hello! We have a local transmission repair shop -- view our logo and shop colors here: http://www.brookvalegears.com

We are the largest volume transmission rebuilder in the area and we need a business card to reflect that. The card needs to have a front and back. The front should display the logo and contact details.

Contact details may include business address, phone number and website url, as well as email: derek@brookvalegears.com

The back could display a Google map with directions to the shop as well as "Free Towing Available"

If needed, address can be featured on the back and not on the front, as we do not want the front to be too wordy. You can also play around with the front only containing the logo with the slogan and the back with all the contact details. Social media icons should also be visible somewhere ( Facebook, Twitter, G+)

Target Market(s)

Car owners who need their transmission repaired or car repaired

Industry/Entity Type

Shop

Font styles to use
Sans Serif

Requirements
Must have
• Must be double sided
• Must have logo in the middle of the front side
• Must have similar grey colors as website is toned

```html
<!DOCTYPE html>
<html lang="en">
<head>
<meta charset="utf-8">
<title>Brookvale Gears – Business Card</title>
<link rel="stylesheet" href="https://fonts.googleapis.com/css2?family=Arimo:wght@400;700&display=swap">
<style>
  :root {
    --backdrop: #d9d6d2;
    --card-black: #141414;
    --card-charcoal: #2a2a2a;
    --brand-red: #7e2224;
    --brand-red-dark: #5e1719;
    --steel-light: #e9e9e9;
    --steel-mid: #b8b8b8;
    --text-light: #f2f2f2;
    --text-soft: #d0d0d0;
    --map-tone: #e6e4df;
  }
  * { box-sizing: border-box; margin: 0; padding: 0; }
  html, body { width: 1200px; height: 1000px; overflow: hidden; }
  body {
    background: var(--backdrop);
    font-family: "Arimo", Arial, sans-serif;
    position: relative;
  }
  .card {
    position: absolute;
    width: 770px;
    height: 440px;
    left: 215px;
    overflow: hidden;
    border-radius: 4px;
    box-shadow: 0 10px 28px rgba(0,0,0,.25);
    background: linear-gradient(160deg, var(--card-charcoal) 0%, var(--card-black) 55%);
    color: var(--text-light);
  }
  .card--front { top: 40px; }
  .card--back { top: 520px; }

  /* front */
  .front-corner { position: absolute; inset: 0; }
  .business-name {
    position: absolute; left: 40px; top: 42px;
    font-size: 34px; font-weight: 700; letter-spacing: .3px;
  }
  .ribbon {
    position: absolute; left: 0; top: 112px;
    height: 54px; width: 320px;
    background: var(--brand-red);
    clip-path: polygon(0 0, 100% 0, 88% 50%, 100% 100%, 0 100%);
    font-size: 30px; font-weight: 700;
    line-height: 54px; padding-left: 40px;
  }
  .phone {
    position: absolute; left: 40px; top: 258px;
    font-size: 50px; font-weight: 700; color: var(--text-soft);
  }
  .contact-lines {
    position: absolute; left: 40px; top: 330px;
    font-size: 24px; line-height: 32px; color: var(--text-soft);
    list-style: none;
  }
  .brand-mark {
    position: absolute; left: 430px; top: 50px;
    width: 300px; height: 300px; border-radius: 50%;
    background: radial-gradient(circle at 40% 35%, var(--steel-light), var(--steel-mid));
    display: flex; align-items: center; justify-content: center;
    box-shadow: 0 0 0 22px var(--card-black);
  }
  .brand-mark__name {
    font-size: 40px; font-weight: 700; color: var(--brand-red);
    text-align: center; line-height: 1.1;
  }

  /* back */
  .address-block {
    position: absolute; left: 40px; top: 34px;
    font-size: 24px; line-height: 30px; color: var(--text-light);
  }
  .address-block p + p { margin-top: 22px; }
  .link-band {
    position: absolute; left: 0; bottom: 0; width: 470px; height: 150px;
    background: linear-gradient(180deg, var(--brand-red), var(--brand-red-dark));
  }
  .link-list {
    position: absolute; left: 22px; bottom: 24px; width: 440px;
    list-style: none; font-size: 17px; line-height: 34px; color: var(--text-light);
    white-space: nowrap;
  }
  .link-list li { display: flex; align-items: center; gap: 10px; }
  .link-list .icon-square {
    width: 22px; height: 22px; background: var(--text-light); border-radius: 3px; flex: none;
  }
  .map-area {
    position: absolute; right: 22px; bottom: 24px;
    width: 262px; height: 250px;
    background: linear-gradient(135deg, var(--map-tone), #cfcdc8);
    border: 3px solid var(--brand-red);
  }
</style>
</head>
<body>
  <section class="card card--front" aria-label="Card front">
    <svg class="front-corner" width="770" height="440" viewBox="0 0 770 440" aria-hidden="true">
      <polygon points="420,0 770,0 770,300" fill="var(--brand-red)"/>
    </svg>
    <h1 class="business-name">Brookvale Gears</h1>
    <div class="ribbon">Free Estimates</div>
    <p class="phone">704-555-0187</p>
    <ul class="contact-lines">
      <li>derek@brookvalegears.com</li>
      <li>www.brookvalegears.com</li>
    </ul>
    <div class="brand-mark">
      <span class="brand-mark__name">Brookvale<br>Gears</span>
    </div>
  </section>

  <section class="card card--back" aria-label="Card back">
    <div class="address-block">
      <p>Brookvale Gears<br>48 Foundry Lane<br>Millbrook, NC 28990</p>
      <p>We are located right off of<br>Route 9, just minutes from<br>I-312 in Millbrook</p>
    </div>
    <div class="link-band"></div>
    <ul class="link-list">
      <li><span class="icon-square"></span>https://www.brookvalegears.com/news</li>
      <li><span class="icon-square"></span>https://www.brookvalegears.com/updates</li>
      <li><span class="icon-square"></span>https://www.brookvalegears.com/reviews/millbrook</li>
    </ul>
    <div class="map-area" role="img" aria-label="Street map showing the route from the interstate to the shop"></div>
  </section>
</body>
</html>
```